Faithful in the Small...Powerful together

Capital Campaign for Brightwell Chapel...need it engaging..spiritually based with pics of the community etc...

Target Market(s)

church congregation and sphere of influence

Industry/Entity Type

religious

Colors
EB3D1F
EC4F4E
F09395
F8D3D4
FCEDEE

Requirements
Must have
• tier levels..engaging scripture and photos

```html
<!DOCTYPE html>
<html lang="en">
<head>
<meta charset="utf-8">
<title>Brightwell Chapel – Faithful in the Small, Powerful Together</title>
<link href="https://fonts.googleapis.com/css2?family=Jost:wght@400;500;600&family=Arimo:wght@400&family=Barlow+Condensed:wght@300;600&display=swap" rel="stylesheet">
<style>
  :root {
    --red: #EB2A1F;
    --red-deep: #D8231A;
    --ink: #141414;
    --ink-soft: #191919;
    --white: #ffffff;
    --sky: #5e93d6;
    --sky-light: #8fb5e4;
    --brick: #8f6a5c;
    --lawn: #7d7266;
  }
  * { margin: 0; padding: 0; box-sizing: border-box; }
  html, body { width: 1200px; height: 848px; overflow: hidden; background: var(--ink); }
  .cover {
    position: relative;
    width: 1200px;
    height: 848px;
    overflow: hidden;
    background: var(--red);
  }
  .back-panel {
    position: absolute; left: 0; top: 0;
    width: 594px; height: 848px;
    background: var(--red);
  }
  .front-photo {
    position: absolute; left: 594px; top: 0;
    width: 606px; height: 700px;
    background: linear-gradient(180deg, var(--sky) 0%, var(--sky-light) 40%, #a9a3a3 58%, var(--brick) 78%, var(--lawn) 100%);
  }
  .swoosh {
    position: absolute; left: 0; top: 0;
    width: 1200px; height: 848px;
  }
  .scripture {
    position: absolute; left: 0; width: 594px;
    text-align: center;
    color: var(--white);
  }
  .scripture .mark {
    font-family: 'Jost', sans-serif;
    font-size: 22px; line-height: 1;
    display: block; margin-bottom: 8px;
  }
  .scripture blockquote {
    font-family: 'Jost', sans-serif;
    font-weight: 400;
    font-size: 24px;
    line-height: 27px;
  }
  .scripture cite {
    display: block;
    font-family: 'Arimo', sans-serif;
    font-style: normal;
    font-size: 15px;
    margin-top: 6px;
  }
  .scripture--luke { top: 42px; }
  .scripture--psalm { top: 178px; }
  .community-photo {
    position: absolute;
    left: 126px; top: 366px;
    width: 312px; height: 312px;
    border-radius: 50%;
    border: 5px solid var(--red);
    background: linear-gradient(180deg, #d7d3cc 0%, #cfc2b8 40%, #9fb0cc 70%, #6f7f9c 100%);
  }
  .website {
    position: absolute; left: 0; top: 743px; width: 594px;
    text-align: center;
    font-family: 'Jost', sans-serif;
    font-size: 24px;
    color: var(--white);
    letter-spacing: 0.2px;
  }
  .brand-name {
    position: absolute; left: 644px; top: 110px;
    font-family: 'Jost', sans-serif;
    font-weight: 600;
    font-size: 34px;
    color: var(--ink);
  }
  .tagline {
    position: absolute; left: 666px; top: 712px;
    font-family: 'Barlow Condensed', sans-serif;
    font-size: 52px;
    line-height: 44px;
    letter-spacing: 0.6px;
    color: var(--red);
    text-transform: uppercase;
  }
  .tagline strong { font-weight: 600; }
  .tagline .light { font-weight: 300; }
</style>
</head>
<body>
<main class="cover">
  <div class="back-panel"></div>
  <div class="front-photo" role="img" aria-label="Photo of a red-brick church with white columns and steeple under a blue sky, a banner flag on the lawn and a woman in a green dress singing into a microphone"></div>

  <svg class="swoosh" viewBox="0 0 1200 848" aria-hidden="true">
    <path d="M0,462 C220,525 420,615 600,638 C850,668 1080,600 1200,476 L1200,848 L0,848 Z" fill="var(--ink)"/>
    <path d="M594,640 C850,670 1080,602 1200,478 L1200,848 L594,848 Z" fill="var(--ink-soft)"/>
    <path d="M0,478 C220,542 420,632 600,654 C850,684 1085,614 1200,500" fill="none" stroke="var(--red)" stroke-width="6"/>
    <path d="M0,500 C220,568 420,660 610,682 C860,710 1095,640 1200,548" fill="none" stroke="var(--red)" stroke-width="14"/>
    <path d="M0,520 C220,592 420,684 620,704 C870,728 1100,662 1200,585" fill="none" stroke="var(--red-deep)" stroke-width="4"/>
  </svg>

  <section class="scripture scripture--luke">
    <span class="mark">"</span>
    <blockquote>Whoever is faithful in very little<br>is also faithful in much.</blockquote>
    <cite>- Luke 16:10</cite>
  </section>

  <section class="scripture scripture--psalm">
    <span class="mark">"</span>
    <blockquote>How good and pleasant it is<br>when God's people live together in unity</blockquote>
    <cite>- Psalm 133:1</cite>
  </section>

  <div class="community-photo" role="img" aria-label="Photo of three smiling volunteers standing behind a cart full of donated goods in a hallway"></div>

  <p class="website">www.brightwellchapel.org</p>

  <p class="brand-name">Brightwell Chapel</p>

  <h1 class="tagline">
    <strong>Faithful</strong> <span class="light">in the small,</span><br>
    <strong>Powerful together.</strong>
  </h1>
</main>
</body>
</html>
```